Harbinger Slabworks, Inc. Business Card

Create a business card that is eye catching and based around concrete sawcutting. I've attached our current business card and logo for reference. We like aspects of the current business card, but it is starting to feel very loud and lost. We would like something that is still fun but is more modern and streamlined.

```html
<!DOCTYPE html>
<html lang="en">
<head>
<meta charset="utf-8">
<title>Harbinger Slabworks, Inc. Business Card</title>
<link href="https://fonts.googleapis.com/css2?family=Montserrat:wght@400;500;700&display=swap" rel="stylesheet">
<style>
  :root {
    --stage: #e6e6e8;
    --card: #ffffff;
    --red: #c8202d;
    --navy: #1f2a5c;
    --ink: #2b2b2b;
  }
  * { margin: 0; padding: 0; box-sizing: border-box; }
  html, body { width: 1200px; height: 1108px; overflow: hidden; }
  body {
    background: var(--stage);
    font-family: "Montserrat", Arial, sans-serif;
    display: flex;
    align-items: center;
    justify-content: center;
    gap: 60px;
  }
  .card {
    width: 400px;
    height: 700px;
    background: var(--card);
    border-radius: 30px;
    box-shadow: 0 12px 30px rgba(0,0,0,0.18);
    display: flex;
    flex-direction: column;
    align-items: center;
    text-align: center;
  }
  .brand { display: flex; flex-direction: column; align-items: center; gap: 18px; }
  .brand-mark { width: 190px; height: 190px; border-radius: 50%; background: var(--navy); }
  .brand-name {
    color: var(--navy);
    font-weight: 700;
    font-size: 19px;
    letter-spacing: 0.5px;
    text-transform: uppercase;
  }
  .card-front { padding-top: 56px; }
  .person-name {
    margin-top: 58px;
    color: var(--red);
    font-weight: 700;
    font-size: 30px;
    letter-spacing: 0.5px;
  }
  .person-title { color: var(--ink); font-size: 20px; margin-top: 2px; }
  .icon-row {
    margin-top: 26px;
    display: flex;
    align-items: center;
    gap: 10px;
    width: 320px;
  }
  .rule { flex: 1; height: 2px; background: var(--red); }
  .icon {
    width: 36px; height: 36px;
    border-radius: 9px;
    background: var(--red);
    display: flex; align-items: center; justify-content: center;
  }
  .icon svg { width: 22px; height: 22px; }
  .contact { margin-top: 22px; color: var(--ink); font-size: 20px; line-height: 1.35; font-style: normal; }
  .divider { width: 320px; height: 2px; background: var(--red); margin: 18px 0 14px; }
  .address { color: var(--ink); font-size: 20px; line-height: 1.35; font-style: normal; }
  .card-back { justify-content: center; padding-bottom: 80px; }
  .card-back .brand-mark { width: 250px; height: 250px; }
  .card-back .brand-name { font-size: 21px; }
</style>
</head>
<body>
  <section class="card card-front">
    <div class="brand">
      <div class="brand-mark"></div>
      <div class="brand-name">Harbinger Slabworks, Inc.</div>
    </div>
    <h1 class="person-name">CALVIN REYES</h1>
    <p class="person-title">Managing Director</p>
    <div class="icon-row">
      <span class="rule"></span>
      <span class="icon" aria-label="phone">
        <svg viewBox="0 0 24 24"><path fill="#fff" d="M6.6 10.8a15 15 0 0 0 6.6 6.6l2.2-2.2c.3-.3.7-.4 1-.2 1.1.4 2.3.6 3.6.6.6 0 1 .4 1 1V20c0 .6-.4 1-1 1A17 17 0 0 1 3 4c0-.6.4-1 1-1h3.5c.6 0 1 .4 1 1 0 1.3.2 2.5.6 3.6.1.3 0 .7-.2 1z"/></svg>
      </span>
      <span class="icon" aria-label="email">
        <svg viewBox="0 0 24 24"><rect x="3" y="6" width="18" height="12" rx="1.5" fill="#fff"/><path d="M3.5 6.5 12 13l8.5-6.5" fill="none" stroke="#c8202d" stroke-width="1.6"/></svg>
      </span>
      <span class="icon" aria-label="website">
        <svg viewBox="0 0 24 24"><circle cx="12" cy="12" r="8.5" fill="none" stroke="#fff" stroke-width="2"/><path d="M3.5 12h17M12 3.5c3 3 3 14 0 17M12 3.5c-3 3-3 14 0 17" fill="none" stroke="#fff" stroke-width="1.5"/></svg>
      </span>
      <span class="rule"></span>
    </div>
    <address class="contact">
      555 014 2230<br>
      info@harbingerslab.com<br>
      www.harbingerslab.com
    </address>
    <div class="divider"></div>
    <address class="address">
      1840 Quarry Ridge Road<br>
      Stonefield CA 90017
    </address>
  </section>

  <section class="card card-back">
    <div class="brand">
      <div class="brand-mark"></div>
      <div class="brand-name">Harbinger Slabworks, Inc.</div>
    </div>
  </section>
</body>
</html>
```